Updated Business Card Design more modern and eye catching

looking for something more dynamic than the sterile card we have now. Please take a look at our web site www.quarvinstores.net to see what we do. only looking for the front side of the card for now. I've also attached a sample of a card with raised spot uv ink - it might be cool to incorporate something like that. Card should be bold yet serious. No frilly or scrolly stuff on it.
Updates
Target Market(s)
We do decor and signage for retail business and supermarkets. Our new name should reflect that we're hip but serious.
Contact Information for Business Card
standard business card size - horizontal preferred
Font styles to use
Requirements
Must have
- Current logo and colors cannot be changed.
Nice to have
- Must have information shown on existing card but open to some changes. Okay to consider spot uv.
Should not have
- Not busy with pictures in the background.

```html
<!DOCTYPE html>
<html lang="en">
<head>
<meta charset="utf-8">
<title>Quarvin Stores – Business Card</title>
<link rel="stylesheet" href="https://fonts.googleapis.com/css2?family=Michroma&family=Roboto:wght@400;500&display=swap">
<style>
  :root {
    --backdrop: #1c1c1d;
    --card: #111112;
    --card-edge: #1e1e20;
    --gold: #b3a552;
    --white: #f2f2f2;
    --rule: #cfcfcf;
  }
  html, body {
    margin: 0;
    width: 1200px;
    height: 1200px;
    overflow: hidden;
    background: var(--backdrop);
  }
  .business-card {
    position: absolute;
    left: 100px;
    top: 314px;
    width: 1000px;
    height: 571px;
    background: linear-gradient(160deg, var(--card-edge) 0%, var(--card) 55%, #0c0c0d 100%);
    box-shadow: 0 18px 40px rgba(0,0,0,0.55);
    font-family: "Roboto", Arial, sans-serif;
    color: var(--white);
  }
  .brand {
    position: absolute;
    left: 70px;
    top: 66px;
    display: flex;
    align-items: center;
    gap: 22px;
  }
  .brand-square {
    width: 34px;
    height: 34px;
    background: var(--gold);
  }
  .brand-name {
    font-family: "Michroma", "Arial Black", sans-serif;
    font-size: 36px;
    letter-spacing: 3px;
    color: var(--gold);
    line-height: 1;
  }
  .person {
    position: absolute;
    left: 70px;
    top: 222px;
    font-family: "Michroma", Arial, sans-serif;
  }
  .person-name {
    font-size: 30px;
    letter-spacing: 2px;
    margin: 0;
  }
  .person-name .first { color: var(--gold); }
  .person-name .last { color: var(--white); }
  .person-title {
    font-size: 19px;
    letter-spacing: 5px;
    color: var(--gold);
    margin: 8px 0 0;
  }
  .divider {
    position: absolute;
    left: 60px;
    right: 70px;
    top: 318px;
    height: 2px;
    background: var(--rule);
  }
  .contact-list {
    position: absolute;
    left: 70px;
    top: 340px;
    margin: 0;
    padding: 0;
    list-style: none;
    font-size: 23px;
    letter-spacing: 1px;
  }
  .contact-list li {
    display: flex;
    align-items: center;
    gap: 16px;
    height: 40px;
  }
  .contact-list svg {
    width: 24px;
    height: 24px;
    fill: none;
    stroke: var(--gold);
    stroke-width: 2;
  }
  .address {
    position: absolute;
    right: 70px;
    top: 345px;
    text-align: right;
    font-size: 24px;
    line-height: 1.45;
    letter-spacing: 1px;
  }
</style>
</head>
<body>
  <section class="business-card">
    <div class="brand">
      <div class="brand-square"></div>
      <div class="brand-name">QUARVIN STORES</div>
    </div>

    <div class="person">
      <p class="person-name"><span class="first">MARLA</span> <span class="last">DENNING</span></p>
      <p class="person-title">VICE-PRESIDENT</p>
    </div>

    <div class="divider"></div>

    <ul class="contact-list">
      <li>
        <svg viewBox="0 0 24 24" aria-hidden="true"><rect x="6" y="2" width="12" height="20" rx="2"/><line x1="9" y1="18" x2="15" y2="18"/></svg>
        555.318.4076
      </li>
      <li>
        <svg viewBox="0 0 24 24" aria-hidden="true"><path d="M3 9c0-3 4-5 9-5s9 2 9 5l-4 1-1-3H8L7 10z"/><rect x="5" y="12" width="14" height="8" rx="1"/></svg>
        555.260.1189ext.3
      </li>
      <li>
        <svg viewBox="0 0 24 24" aria-hidden="true"><rect x="2" y="5" width="20" height="14"/><polyline points="2,5 12,13 22,5"/></svg>
        Marla@QuarvinStores.net
      </li>
      <li>
        <svg viewBox="0 0 24 24" aria-hidden="true"><circle cx="12" cy="12" r="10"/><ellipse cx="12" cy="12" rx="4" ry="10"/><line x1="2" y1="12" x2="22" y2="12"/></svg>
        www.quarvinstores.net
      </li>
    </ul>

    <address class="address" style="font-style:normal">
      4170 Commerce Park Way<br>
      Harbor Lakes, FL 34010
    </address>
  </section>
</body>
</html>
```